Lady Marisol's Reserve Aged Bramblewick Rum LABEL

Tallpine Hollow Distillery is looking for a label for our new product (Lady Marisol's Reserve). This will be a barrel aged Rum that is distilled, bottled, and aged in small batches in Belmont, NC just outside of Charlotte, North Carolina. In the attached file (drink recipes) you will see the Product that we currently sell (Bramblewick Rum). The new product does not have to be the same style, but we would like to maintain some brand relevance. There are some other attachments to give you an idea about the look of the company. Also attached is a picture of the dark rum in the bottle. This is what the label will go onto.

-The label will most likely be printed on craft paper stock.

Industry/Entity Type

It Company

Requirements
Must have
• We need the following in the new label
-Company Name= Tallpine Hollow Distillery
-Product name= Lady Marisol's Reserve
-Product sub-name= Aged Bramblewick Rum
-Product description= Distilled Bottled and Aged by Tallpine Hollow Distillery
Nice to have
• We would like to incorporate a rendering of Lady Marisol or just a crown. We think this is important because Charlotte, NC is named after her.

```html
<!DOCTYPE html>
<html lang="en">
<head>
<meta charset="utf-8">
<title>Lady Marisol's Reserve — Aged Bramblewick Rum Label</title>
<link rel="stylesheet" href="https://fonts.googleapis.com/css2?family=Cinzel:wght@400;600;700&display=swap">
<style>
  :root {
    --backdrop: #f3f1ee;
    --parchment-light: #e9d7a8;
    --parchment-mid: #c9a265;
    --parchment-dark: #6e4a1e;
    --ink: #111010;
    --oval-black: #0a0908;
    --rim-copper: #b8662a;
    --rim-gold: #e8c167;
    --gold-text: #e6c766;
    --cream-text: #f4efe4;
    --banner-maroon: #4a0f0c;
    --banner-gold: #e2c47a;
  }
  * { margin: 0; padding: 0; box-sizing: border-box; }
  html, body { width: 1200px; height: 855px; overflow: hidden; background: var(--backdrop); }
  .canvas { position: relative; width: 1200px; height: 855px; }

  .label { position: absolute; left: 172px; top: 250px; width: 856px; height: 342px; }
  .label__paper { position: absolute; inset: 0; width: 856px; height: 334px; }

  .label__company {
    position: absolute; left: 0; right: 0; top: 10px;
    text-align: center; font-family: "Cinzel", serif; font-weight: 600;
    color: var(--ink); font-size: 33px; line-height: 38px; letter-spacing: 0.5px;
  }

  .seal {
    position: absolute; left: 163px; top: 82px; width: 264px; height: 212px;
    left: calc(50% - 137px);
    border-radius: 50%;
    background: radial-gradient(ellipse at 50% 40%, #1a1714 0%, var(--oval-black) 70%);
    border: 5px solid var(--rim-copper);
    box-shadow: 0 0 0 2px var(--rim-gold), inset 0 0 0 2px #6b3413, 0 3px 8px rgba(40,20,0,.45);
    text-align: center; font-family: "Cinzel", serif;
  }
  .seal__crown {
    display: block; width: 30px; height: 20px; margin: 12px auto 0;
    background: linear-gradient(#f2d77c, #b98a2c); border-radius: 2px;
  }
  .seal__product {
    color: var(--gold-text); font-size: 22px; line-height: 29px; margin-top: 3px;
  }
  .seal__divider { position: relative; height: 14px; margin: 6px 26px 0; }
  .seal__divider-line {
    position: absolute; left: 26px; right: 26px; top: 6px; height: 2px; background: var(--rim-gold);
  }
  .seal__flourish {
    position: absolute; top: 0; width: 22px; height: 14px; border-radius: 3px;
    background: linear-gradient(#f2d77c, #b98a2c);
  }
  .seal__flourish--left { left: 0; }
  .seal__flourish--right { right: 0; }
  .seal__subname {
    color: var(--cream-text); font-size: 16px; line-height: 20px; margin-top: 2px;
  }

  .label__banner {
    position: absolute; left: 133px; top: 297px; width: 617px; height: 38px;
    background: linear-gradient(var(--banner-maroon), #2f0807);
    border-radius: 7px;
    display: flex; align-items: center; justify-content: center;
    font-family: "Cinzel", serif; font-size: 15.5px; letter-spacing: 0.4px;
    color: var(--banner-gold); white-space: nowrap;
  }
</style>
</head>
<body>
<main class="canvas">
  <section class="label" aria-label="Lady Marisol's Reserve rum label">
    <svg class="label__paper" viewBox="0 0 856 334" role="img" aria-label="Aged parchment paper with torn edges and faint botanical sketches">
      <defs>
        <radialGradient id="parchment" cx="50%" cy="45%" r="65%">
          <stop offset="0" stop-color="var(--parchment-light)"/>
          <stop offset="0.55" stop-color="var(--parchment-mid)"/>
          <stop offset="1" stop-color="var(--parchment-dark)"/>
        </radialGradient>
      </defs>
      <path fill="url(#parchment)" d="M0 6 L40 4 L70 9 L110 3 L160 8 L210 2 L260 7 L300 4 L350 9 L400 3 L450 8 L500 2 L540 7 L590 3 L640 8 L690 4 L730 10 L770 3 L810 7 L856 2 L856 326 L820 330 L780 324 L740 331 L700 326 L120 326 L80 330 L40 324 L0 330 Z"/>
    </svg>

    <h1 class="label__company">Tallpine Hollow<br>Distillery</h1>

    <div class="seal">
      <span class="seal__crown" role="img" aria-label="Small gold crown"></span>
      <h2 class="seal__product">Lady<br>Marisol's<br>Reserve</h2>
      <div class="seal__divider">
        <span class="seal__flourish seal__flourish--left" role="img" aria-label="Gold fleur-de-lis ornament"></span>
        <span class="seal__divider-line"></span>
        <span class="seal__flourish seal__flourish--right" role="img" aria-label="Gold fleur-de-lis ornament"></span>
      </div>
      <p class="seal__subname">Aged Bramblewick<br>Rum</p>
    </div>

    <p class="label__banner">Distilled Bottled and Aged by Tallpine Hollow Distillery</p>
  </section>
</main>
</body>
</html>
```